Business card for Luxury Portable Restroom Trailer company

We are a Luxury Portable Restroom Trailer Company Called PELIKAR HIRES. Based in Orange County California. We provide portable restroom trailers for events, such as, Weddings, Concerts, Charity events, Sporting events, Tournaments, Corporate events, ect. We rent and Sell the Luxury restrooms. Our colors are white, grey, and Orange. As you will see in the logo we uploaded.
There are 2 people in the company so the names and titles will change for the 3 people but card will remain the same. Here is the information for each Person: Dennis Moyle CFO 555 018-3647
next Person: Wesley Tanford VP 555 018-3647
Next Person: Miles Tanford CEO 555 018-3647
Information to include on the card: Luxury Restroom Trailers Rental and Sales. Weddings, Concerts, Charity, Sporting and Corp. Events.

```html
<!DOCTYPE html>
<html lang="en">
<head>
<meta charset="utf-8">
<title>Pelikar Hires – Business Card</title>
<link rel="stylesheet" href="https://fonts.googleapis.com/css2?family=Prompt:ital,wght@0,600;0,700;1,600&display=swap">
<style>
  :root {
    --backdrop: #b6b6b6;
    --orange: #f06a28;
    --orange-soft: #f59f6e;
    --white: #ffffff;
    --grey: #55565a;
    --brown: #775c52;
    --shadow: rgba(0,0,0,0.35);
  }
  * { margin: 0; padding: 0; box-sizing: border-box; }
  html, body { width: 1200px; height: 1200px; overflow: hidden; }
  body {
    background: var(--backdrop);
    position: relative;
    font-family: "Prompt", sans-serif;
  }
  .card {
    position: absolute;
    left: 238px;
    width: 729px;
    height: 416px;
    overflow: hidden;
    box-shadow: 6px 8px 6px var(--shadow);
  }
  .card-front { top: 131px; background: var(--white); }
  .card-back { top: 604px; background: var(--orange); }

  .side-tab { position: absolute; top: 114px; }
  .side-tab--left { left: 0; }
  .side-tab--right { right: 0; }

  .brand-ring { position: absolute; left: 244px; top: 30px; }

  .front-name {
    position: absolute;
    left: 0; right: 0;
    top: 288px;
    text-align: center;
    font-weight: 700;
    font-size: 50px;
    letter-spacing: 2px;
    color: var(--orange);
    line-height: 1;
  }

  .back-name {
    position: absolute;
    left: 58px;
    top: 36px;
    font-weight: 700;
    font-size: 27px;
    letter-spacing: 1px;
    color: var(--white);
    line-height: 1;
  }

  .brand-mark-area {
    position: absolute;
    left: 470px;
    top: 36px;
    width: 259px;
    height: 256px;
    background: var(--orange-soft);
    border-radius: 128px 0 0 128px;
    opacity: 0.9;
  }

  .contact-list {
    position: absolute;
    left: 58px;
    top: 144px;
    list-style: none;
  }
  .contact-list li {
    position: relative;
    padding-left: 24px;
    font-weight: 700;
    font-size: 25px;
    line-height: 43px;
    color: var(--white);
    white-space: nowrap;
  }
  .contact-list li::before {
    content: "";
    position: absolute;
    left: 5px;
    top: 17px;
    width: 10px;
    height: 10px;
    border-radius: 50%;
    background: var(--white);
  }

  .tagline-band {
    position: absolute;
    left: 0; right: 0;
    top: 310px;
    height: 77px;
    background: var(--brown);
    display: flex;
    flex-direction: column;
    justify-content: center;
    align-items: center;
    color: var(--white);
    font-style: italic;
    font-weight: 600;
    font-size: 19px;
    line-height: 27px;
  }
</style>
</head>
<body>
  <section class="card card-front" aria-label="Card front">
    <svg class="side-tab side-tab--left" width="45" height="189" viewBox="0 0 45 189">
      <polygon points="0,0 45,40 45,148 0,189" fill="var(--orange)"/>
    </svg>
    <svg class="side-tab side-tab--right" width="45" height="189" viewBox="0 0 45 189">
      <polygon points="45,0 0,40 0,148 45,189" fill="var(--orange)"/>
    </svg>
    <svg class="brand-ring" width="240" height="240" viewBox="0 0 240 240" aria-hidden="true">
      <circle cx="120" cy="120" r="108" fill="none" stroke="var(--orange)" stroke-width="8"/>
    </svg>
    <h1 class="front-name">PELIKAR HIRES</h1>
  </section>

  <section class="card card-back" aria-label="Card back">
    <div class="brand-mark-area" role="img" aria-label="Large faint brand decoration"></div>
    <h2 class="back-name">PELIKAR HIRES</h2>
    <ul class="contact-list">
      <li>Dennis Moyle CFO 555 018-3647</li>
      <li>Wesley Tanford VP 555 018-3647</li>
      <li>Miles Tanford CEO 555 018-3647</li>
    </ul>
    <div class="tagline-band">
      <p>Luxury Restroom Trailers Rental and Sales.</p>
      <p>Weddings, Concerts, Charity, Sporting and Corp. Events.</p>
    </div>
  </section>
</body>
</html>
```